Meal Prep Business in need of flyer

We are a company specializing in healthy meals and meals prep. We would like an eye catching flyer to post in town and in gyms. We would like the flyer to include Local(Labrador West) next day delivery. Shipping to Churchill Falls, Goose Bay and St. John's, NL. Customized meal plans.

I would like something that highlights our sponsored athletes as well Marla Dempsey - National Figure Competitor and 2015 KQFTU Overall Figure Champ and Tess Worrick National Bikini Competitor and 2016 KQFTU Overall Bikini Champ.
I would like to have the WE-SHOP WE COOK WE DELIVER and our email oliver@fernvaleplates.com.

The final design should communicate how we save you time while living a healthier or fitness orientated lifestyle and drive people to our website. Website is www.fernvaleplates.com

Target Market(s)

Fitness, meal prep, people looking to eat heathier, people looking to lose weight. and people looking to save time

Industry/Entity Type

Nutrition

Contact Information for Business Card

We are a company specializing in healthy meals and meals prep. We would like an eye catching business card . We would like the flyer to include Local(Labrador West) next day delivery.
Shipping to Churchill Falls,
Goose Bay and
St. John's, NL.

We do Customized meal plans.
i would like something that highlights our sponsored athletes as well Marla Dempsey - National Figure Competitor and 2015 KQFTU Overall Figure Champ and Tess Worrick National Bikini Competitor and 2016 KQFTU Overall Classic Bikini Champ. I would like to have the WE-SHOP WE COOK WE DELIVER, phone number 7090461-5382 and our email oliver@fernvaleplates.com.The final design should communicate living a healthier lifestyle and drive people to our website. Website is www.fernvaleplate.com

Colors
3176b5
0255a3
33a6d7
0492cd

Requirements
Must have
• Flyer - Logo, Next day shipping, shipping to Goose Bay, Churchill Falls & St John's, NL. Sponsored athletes, website, slogan, customized meals plans, a couple of picture of our meals
• business card - logo, website, slogan, phone number, email, next day shipping, shipping to Goose Bay, Churchill Falls & St John's, NL,
Nice to have
• Flyer - Sponsored athletes pictures, flyer to be a template to change pics and any info
• Business card - sponsored athletes, picture of our meals

```html
<!DOCTYPE html>
<html lang="en">
<head>
<meta charset="utf-8">
<title>Fernvale Plates – We Shop, We Cook, We Deliver</title>
<link rel="stylesheet" href="https://fonts.googleapis.com/css2?family=Open+Sans:wght@700;800&family=Roboto+Condensed:wght@400;700&family=Roboto:wght@500;700&display=swap">
<style>
  :root{
    --blue-deep:#0255a3;
    --blue-mid:#3176b5;
    --blue:#0492cd;
    --blue-light:#33a6d7;
    --text-blue:#1b8fd2;
    --white:#ffffff;
    --paper:#f4f5f6;
    --paper-shade:#e4e7ea;
    --ink:#111111;
    --stage:#e9eaec;
  }
  *{margin:0;padding:0;box-sizing:border-box}
  html,body{width:900px;height:1200px;overflow:hidden;background:var(--stage)}
  .canvas{position:relative;width:900px;height:1200px;overflow:hidden}
  .flyer{
    position:absolute;left:26px;top:0;
    width:625px;height:885px;
    transform:scale(1.3559);transform-origin:0 0;
    overflow:hidden;background:var(--paper);
  }
  .flyer-shapes{position:absolute;inset:0;width:625px;height:885px}
  .slogan{position:absolute;color:var(--white);font-family:"Open Sans",sans-serif}
  .slogan-we{left:236px;top:389px;font-size:122px;font-weight:800;line-height:1;letter-spacing:-4px}
  .slogan-verbs{left:440px;top:404px;font-size:35px;font-weight:700;line-height:32.5px;letter-spacing:.3px}
  .services{position:absolute;inset:0;font-family:"Roboto Condensed",sans-serif;font-size:17.5px;color:var(--text-blue);line-height:22px}
  .service{position:absolute;white-space:nowrap}
  .tick{position:absolute;width:15px;height:13px}
  .services-divider{position:absolute;left:312px;top:564px;width:1px;height:66px;background:#9fb4c6}
  .athlete-name{position:absolute;font-family:"Roboto Condensed",sans-serif;font-size:18px;color:var(--white);white-space:nowrap}
  .athlete-title{position:absolute;font-family:"Roboto Condensed",sans-serif;font-size:8.2px;line-height:11px;color:var(--white);white-space:nowrap}
  .align-right{text-align:right}
  .contact{position:absolute;font-family:"Roboto",sans-serif;font-weight:700;font-size:16.5px;color:var(--white);white-space:nowrap}
  .contact-divider{position:absolute;left:317px;top:833px;width:1px;height:34px;background:rgba(255,255,255,.6)}
</style>
</head>
<body>
<div class="canvas">
  <div class="flyer">
    <svg class="flyer-shapes" viewBox="0 0 625 885" xmlns="http://www.w3.org/2000/svg">
      <defs>
        <linearGradient id="paperFade" x1="0" y1="0" x2="0" y2="1">
          <stop offset="0" stop-color="var(--white)"/>
          <stop offset="1" stop-color="var(--paper-shade)"/>
        </linearGradient>
        <linearGradient id="heroBlue" x1="0" y1="0" x2="1" y2="0">
          <stop offset="0" stop-color="var(--blue-deep)"/>
          <stop offset=".55" stop-color="#0a6fbf"/>
          <stop offset="1" stop-color="var(--blue-light)"/>
        </linearGradient>
        <linearGradient id="footerBlue" x1="0" y1="0" x2="1" y2="0">
          <stop offset="0" stop-color="var(--blue-light)"/>
          <stop offset="1" stop-color="var(--blue)"/>
        </linearGradient>
        <radialGradient id="noodleTones" cx=".42" cy=".42" r=".75">
          <stop offset="0" stop-color="#e0c17a"/>
          <stop offset=".45" stop-color="#c89f55"/>
          <stop offset=".8" stop-color="#6b5233"/>
          <stop offset="1" stop-color="#241b16"/>
        </radialGradient>
        <radialGradient id="mealTones" cx=".45" cy=".45" r=".65">
          <stop offset="0" stop-color="#e9a45a"/>
          <stop offset=".6" stop-color="#8d6a3f"/>
          <stop offset="1" stop-color="#1d1f22"/>
        </radialGradient>
        <radialGradient id="stageTones" cx=".5" cy=".55" r=".65">
          <stop offset="0" stop-color="#8a5a78"/>
          <stop offset="1" stop-color="#2e2a4f"/>
        </radialGradient>
      </defs>

      <rect class="paper" width="625" height="885" fill="url(#paperFade)"/>

      <path class="footer-band" d="M0,574 C130,640 260,698 400,692 C500,688 575,690 625,680 L625,885 L0,885 Z" fill="url(#footerBlue)"/>

      <path class="hero-band" d="M0,330 C150,440 300,548 450,542 C540,538 595,508 625,494 L625,40 L0,40 Z" fill="url(#heroBlue)"/>

      <path class="hero-accent" d="M0,328 C70,352 150,368 215,372" fill="none" stroke="var(--white)" stroke-width="7"/>

      <g role="img" aria-label="Close-up photo of a stir-fried noodle dish with egg, red pepper and bean sprouts in a dark bowl">
        <path d="M0,0 H625 V58 C565,205 430,330 300,356 C200,374 95,352 0,318 Z" fill="url(#noodleTones)"/>
      </g>

      <g class="meal-thumb">
        <circle cx="342" cy="323" r="58" fill="var(--white)"/>
        <circle cx="342" cy="323" r="53" fill="url(#mealTones)" role="img" aria-label="Meal prep container with sweet potato, broccoli and chicken"/>
      </g>
      <g class="meal-thumb">
        <circle cx="460" cy="271" r="61" fill="var(--white)"/>
        <circle cx="460" cy="271" r="56" fill="url(#mealTones)" role="img" aria-label="Meal prep container with carrots, rice and chicken"/>
      </g>
      <g class="meal-thumb">
        <circle cx="549" cy="203" r="64" fill="var(--white)"/>
        <circle cx="549" cy="203" r="59" fill="url(#mealTones)" role="img" aria-label="Meal prep container with a toasted quesadilla"/>
      </g>

      <g class="athlete-photo">
        <circle cx="239" cy="742" r="70" fill="var(--white)"/>
        <circle cx="239" cy="742" r="65" fill="url(#stageTones)" role="img" aria-label="Sponsored athlete Marla Dempsey posing on stage at a figure competition"/>
      </g>
      <g class="athlete-photo">
        <circle cx="388" cy="742" r="70" fill="var(--white)"/>
        <circle cx="388" cy="742" r="65" fill="url(#stageTones)" role="img" aria-label="Sponsored athlete Tess Worrick posing on stage at a bikini competition"/>
      </g>

      <g class="icon-globe" fill="none" stroke="var(--white)" stroke-width="1.6">
        <circle cx="32" cy="850" r="12.5"/>
        <circle cx="32" cy="850" r="8.5"/>
        <ellipse cx="32" cy="850" rx="3.8" ry="8.5"/>
        <line x1="23.5" y1="850" x2="40.5" y2="850"/>
      </g>
      <g class="icon-mail" fill="none" stroke="var(--white)" stroke-width="1.6">
        <circle cx="350" cy="850" r="12.5"/>
        <rect x="343" y="845" width="14" height="10" rx="1"/>
        <path d="M343,845 L350,851 L357,845"/>
      </g>

      <g class="social-links" fill="var(--white)">
        <rect x="534" y="814" width="16" height="16" rx="3"/>
        <rect x="557" y="814" width="16" height="16" rx="3"/>
        <rect x="583" y="814" width="16" height="16" rx="3"/>
      </g>
    </svg>

    <div class="slogan slogan-we">WE</div>
    <div class="slogan slogan-verbs">SHOP<br>COOK<br>DELIVER</div>

    <div class="services">
      <svg class="tick" style="left:82px;top:557px" viewBox="0 0 16 14"><path d="M1,8 L5.5,12.5 L15,1" fill="none" stroke="var(--ink)" stroke-width="1.8"/></svg>
      <div class="service" style="left:101px;top:561px">Local(Labrador West)<br>next day delivery</div>

      <svg class="tick" style="left:80px;top:610px" viewBox="0 0 16 14"><path d="M1,8 L5.5,12.5 L15,1" fill="none" stroke="var(--ink)" stroke-width="1.8"/></svg>
      <div class="service" style="left:100px;top:614px">Shipping to Churchill Falls</div>

      <div class="services-divider"></div>

      <svg class="tick" style="left:346px;top:565px" viewBox="0 0 16 14"><path d="M1,8 L5.5,12.5 L15,1" fill="none" stroke="var(--ink)" stroke-width="1.8"/></svg>
      <div class="service" style="left:365px;top:569px">Goose Bay and St. John’s</div>

      <svg class="tick" style="left:346px;top:611px" viewBox="0 0 16 14"><path d="M1,8 L5.5,12.5 L15,1" fill="none" stroke="var(--ink)" stroke-width="1.8"/></svg>
      <div class="service" style="left:365px;top:615px">NL. Customized meal plans.</div>
    </div>

    <div class="athlete-name align-right" style="right:463px;top:738px">Marla Dempsey</div>
    <div class="athlete-title align-right" style="right:463px;top:765px">National Figure Competitor and 2015<br>KQFTU Overall Figure Champ</div>

    <div class="athlete-name" style="left:467px;top:740px">Tess Worrick</div>
    <div class="athlete-title" style="left:467px;top:765px">National Bikini Competitor and 2016<br>KQFTU Overall Bikini Champ.</div>

    <div class="contact" style="left:53px;top:840px">www.fernvaleplates.com</div>
    <div class="contact-divider"></div>
    <div class="contact" style="left:372px;top:840px">oliver@fernvaleplates.com.</div>
  </div>
</div>
</body>
</html>
```